Wine Label Design for Marrick Estate

I need a front and back label for a new wine I am making. I am looking for a classic, elegant and serious wine label. I would like the label to be white with blue and black writing. The blue will be the distinction in the label. The color of blue will be unique and catch the eye. The font of the writing will be unique and could also serve as the brand image for Marrick Estate. The label can have a design but should be simple and distinct. I envision the paper quality of the label to textured, high quality and add to the overall image of the label.
The label will be timeless. The price of this wine will be $85.00 a bottle, and the label should match a higher priced wine. This wine is family owned and operated.
The writing on the front and back label will be:

FRONT Label-

Marrick Estate

Howell Mountain

Napa Valley

2022 Cabernet Sauvignon

Back Label-

Cellared and Bottled by Marrick Estate, Larkin Hollow, CA 94599

GOVERNMENT WARNING: (1) According to the Surgeon General, women should not drink alcoholic beverages during pregnancy because of the risk of birth defects. (2) Consumption of alcoholic beverages impairs your ability to drive a car or operate machinery, and may cause health problems.

Alc. 14.5% by Vol.

750 ml

Contains Sulfites

```html
<!DOCTYPE html>
<html lang="en">
<head>
<meta charset="utf-8">
<title>Marrick Estate – Front and Back Labels</title>
<link rel="stylesheet" href="https://fonts.googleapis.com/css2?family=Federo&family=Montserrat:wght@600&family=Cardo&display=swap">
<style>
  :root {
    --backdrop: #e3e3e3;
    --paper: #ffffff;
    --estate-blue: #1d5fae;
    --ornament-tint: #d6e3f3;
    --ink: #2b323c;
    --body-ink: #3a3a3a;
  }
  * { margin: 0; padding: 0; box-sizing: border-box; }
  html, body {
    width: 1200px; height: 1199px; overflow: hidden;
    background: var(--backdrop);
  }
  .label-sheet { position: relative; width: 1200px; height: 1199px; }
  .label {
    position: absolute; top: 247px;
    width: 460px; height: 704px;
    background: var(--paper);
    box-shadow: 0 2px 10px rgba(0,0,0,0.08);
  }
  .label--front { left: 110px; }
  .label--back { left: 630px; }

  .ornament {
    position: absolute; left: 22px; right: 22px;
    background: var(--ornament-tint);
    border: 2px solid var(--estate-blue);
  }
  .label-frame { position: absolute; inset: 0; }

  /* front */
  .wordmark {
    position: absolute; top: 234px; left: 0; right: 0;
    text-align: center; color: var(--ink);
    font-family: "Federo", sans-serif; font-weight: 400;
    line-height: 0.95; font-size: 84px;
  }
  .region {
    position: absolute; left: 62px; right: 62px;
    color: var(--ink);
    font-family: "Montserrat", sans-serif; font-weight: 600;
  }
  .region--mountain { top: 444px; text-align: center; font-size: 22px; letter-spacing: 0.5px; }
  .region--valley {
    top: 472px; display: flex; justify-content: space-between;
    font-size: 17px; padding: 0 8px;
  }
  .region--valley .napa { letter-spacing: 6px; }

  /* back */
  .back-copy {
    position: absolute; left: 0; right: 0;
    text-align: center; color: var(--body-ink);
    font-family: "Cardo", serif;
  }
  .producer { top: 130px; font-size: 18px; line-height: 24px; }
  .warning-title { top: 247px; font-size: 13px; letter-spacing: 0.6px; }
  .warning-text {
    position: absolute; top: 272px; left: 111px; width: 240px;
    font-family: "Cardo", serif; font-size: 12.4px; line-height: 19.5px;
    text-align: justify; color: var(--body-ink);
  }
  .alcohol { top: 462px; font-size: 18px; }
  .volume { top: 496px; font-size: 16px; }
  .sulfites { top: 526px; font-size: 17px; line-height: 22px; }
</style>
</head>
<body>
<main class="label-sheet">

  <section class="label label--front" aria-label="Front label">
    <div class="ornament" style="top:22px;height:196px" role="img" aria-label="Blue line-art ornament with vine scrolls and a grape cluster"></div>

    <svg class="label-frame" width="460" height="704" viewBox="0 0 460 704" aria-hidden="true">
      <g fill="none" stroke="var(--estate-blue)" stroke-width="3">
        <polyline points="34,218 34,500" />
        <polyline points="426,218 426,500" />
        <path d="M12,310 A38,38 0 0 1 12,386" />
        <path d="M448,310 A38,38 0 0 0 448,386" />
        <polyline points="18,342 26,348 18,354" stroke-width="2" />
        <polyline points="442,342 434,348 442,354" stroke-width="2" />
        <polygon class="vintage-badge" points="160,572 230,540 300,572 230,598" stroke-width="2.5" />
      </g>
      <defs>
        <path id="varietal-arc" d="M112,578 Q230,492 348,578" />
      </defs>
      <text class="varietal" font-family="Montserrat, sans-serif" font-weight="600" font-size="15" fill="var(--ink)">
        <textPath href="#varietal-arc" startOffset="50%" text-anchor="middle">CABERNET SAUVIGNON</textPath>
      </text>
      <text class="vintage" x="230" y="578" text-anchor="middle" font-family="Montserrat, sans-serif" font-weight="600" font-size="17" fill="var(--ink)">2022</text>
    </svg>

    <h1 class="wordmark">Marrick<br>Estate</h1>
    <p class="region region--mountain">HOWELL MOUNTAIN</p>
    <p class="region region--valley"><span class="napa">NAPA</span><span>VALLEY</span></p>

    <div class="ornament" style="top:604px;height:80px" role="img" aria-label="Blue line-art ornament with vine scrolls"></div>
  </section>

  <section class="label label--back" aria-label="Back label">
    <div class="ornament" style="top:22px;height:98px" role="img" aria-label="Blue line-art ornament with vine scrolls"></div>

    <p class="back-copy producer">Cellared<br>and Bottled<br>by Marrick Estate,<br>Larkin Hollow, CA 94599</p>
    <p class="back-copy warning-title">GOVERNMENT WARNING:</p>
    <p class="warning-text">(1) According to the Surgeon General, women should not drink alcoholic beverages during pregnancy because of the risk of birth defects.<br>(2) Consumption of alcoholic beverages impairs your ability to drive a car or operate machinery, and may cause health problems.</p>
    <p class="back-copy alcohol">Alc. 14.5% by Vol.</p>
    <p class="back-copy volume">750 ml</p>
    <p class="back-copy sulfites">Contains<br>Sulfites</p>

    <div class="ornament" style="top:586px;height:98px" role="img" aria-label="Blue line-art ornament with vine scrolls"></div>
  </section>

</main>
</body>
</html>
```